FLYERENTWURF  für Make up Ausbildung
FLYERENTWURF für Make up Ausbildung
Zielgruppe
friseure die sich weiterbilden wollen
Aufgabenstellung
zu entwerfen ist ein doppelseitiger flyer in A4, zweimal gefalten.
außenseite:
erste spalte/deckblatt:
das logo (im anhang)
schriftzug: mira beauty schule
eventuell bild kussmund, wenn rechte vorhanden.
zweite spalte/hinterseite:
zahlungsbedingungen (text wird noch beigefügt)
dritte spalte:
personenbild (anhang)
personenbeschreibung (text wird noch beigefügt)
innenseite:
text aus anhang

```html
<!DOCTYPE html>
<html lang="de">
<head>
<meta charset="utf-8">
<title>mira beauty schule – ausbildung make-up</title>
<link href="https://fonts.googleapis.com/css2?family=Tinos:ital,wght@1,400;1,700&display=swap" rel="stylesheet">
<style>
  :root {
    --ink: #f4f2ff;
    --glow: #9a7bff;
    --satin-deep: #05040f;
    --satin-mid: #141046;
    --satin-light: #3a3398;
  }
  html, body { margin: 0; padding: 0; overflow: hidden; background: #000; }
  .flyer {
    position: relative; width: 1200px; height: 848px; overflow: hidden;
    font-family: "Tinos", "Times New Roman", serif; font-style: italic; color: var(--ink);
  }
  .satin {
    position: absolute; inset: 0;
    background:
      linear-gradient(115deg, transparent 8%, rgba(58,51,152,.55) 14%, transparent 20%,
        transparent 30%, rgba(58,51,152,.45) 37%, transparent 44%,
        transparent 52%, rgba(70,62,170,.55) 60%, transparent 67%,
        transparent 76%, rgba(58,51,152,.45) 83%, transparent 90%),
      linear-gradient(160deg, var(--satin-mid), var(--satin-deep) 45%, var(--satin-mid) 70%, var(--satin-deep));
  }
  .column { position: absolute; top: 0; width: 380px; height: 848px; text-align: center; }
  .column--basic { left: 10px; }
  .column--junior { left: 410px; }
  .column--senior { left: 810px; }
  .column > * { position: absolute; left: 0; right: 0; margin: 0; }
  .course-title {
    font-weight: 700; font-size: 25px; letter-spacing: .2px;
    text-shadow: 0 0 6px var(--glow), 0 0 12px var(--glow);
  }
  .section-title {
    font-weight: 700; font-size: 15px;
    text-shadow: 0 0 5px var(--glow), 0 0 10px var(--glow);
  }
  .copy { font-size: 10.5px; line-height: 16px; padding: 0 6px; }
  .topics { list-style: none; padding: 0; font-size: 10.5px; line-height: 16.5px; }
  .dates {
    display: grid; grid-template-columns: 100px 60px; justify-content: center;
    text-align: left; font-size: 10.5px; line-height: 15.2px;
  }
</style>
</head>
<body>
<main class="flyer">
  <div class="satin" role="img" aria-label="dunkelblauer, glänzender satinstoff mit diagonalen lichtfalten"></div>

  <section class="column column--basic">
    <h2 class="course-title" style="top:56px">basic education</h2>
    <p class="copy" style="top:110px">in diesem workshop wird basiswissen vermittelt, mit dem jeder friseur professionell sein beauty-salonprogramm abrunden und das sortiment seiner dienstleistungen erweitern kann.</p>
    <h3 class="section-title" style="top:224px">inhalte auf einen blick</h3>
    <ul class="topics" style="top:246px">
      <li>- produktwissen</li><li>- gesichtsvermessungen</li><li>- optimierung der gesichtsformen</li>
      <li>- augenmakeups</li><li>- makeup für verschiedene augenformen-</li><li>augen-makeup für brillenträgerinnen</li>
      <li>- tages-makeup</li><li>- abend-makeup</li><li>- special-makeup (wimpern kleben,</li><li>aufbringen von glitter und accessoires)</li>
    </ul>
    <h3 class="section-title" style="top:428px">termine</h3>
    <div class="dates" style="top:452px">
      <span>so.,&nbsp; 08.05.2011</span><span>10-18 uhr</span>
      <span>mo.,&nbsp; 09.05.2011</span><span>10-14 uhr</span>
      <span>so.,&nbsp; 15.05.2011</span><span>10-18 uhr</span>
      <span>mo.,&nbsp; 16.05.2011</span><span>10-14 uhr</span>
      <span>so.,&nbsp; 22.05.2011</span><span>10-18 uhr</span>
      <span>mo.,&nbsp; 23.05.2011</span><span>10-14 uhr</span>
      <span>so.,&nbsp; 29.05.2011</span><span>10-18 uhr</span>
      <span>mo.,&nbsp; 30.05.2011</span><span>10-14 uhr</span>
    </div>
    <h3 class="section-title" style="top:604px">voraussetzungen</h3>
    <p class="copy" style="top:625px">dieser kurs ist geeignet für einsteiger und für alle, die vorhandenes wissen auffrischen odervertiefen wollen.</p>
    <h3 class="section-title" style="top:710px">kosten</h3>
    <p class="copy" style="top:735px">€ 990 exkl. mwst</p>
    <h3 class="section-title" style="top:756px">anmeldung</h3>
    <p class="copy" style="top:786px">bis 01.03.2011 mira@lockenglanzsalon.example oder 01 482 17 60</p>
  </section>

  <section class="column column--junior">
    <h2 class="course-title" style="top:53px">junior makeup artist</h2>
    <p class="copy" style="top:120px">junior makeup artists, die diesen kurs absolviert haben, sind in der lage, makeup- und typberatung, foto- und anti-aging-makeup anzubieten. die inhalte befassen sich noch detaillierter als im ersten teil mit farben und formen beim schminken und die techniken werden von der beratung bis zur umsetzung trainiert.</p>
    <h3 class="section-title" style="top:260px">inhalte auf einen blick:</h3>
    <ul class="topics" style="top:284px">
      <li>- haut- anti-aging-makeup</li><li>- foto-makeup</li><li>- schwarz/weiß foto</li><li>-makeup</li>
      <li>- männer-makeup</li><li>- typberatung</li><li>- makeup beratung</li><li>- braut-makeup</li>
    </ul>
    <h3 class="section-title" style="top:426px">termine</h3>
    <div class="dates" style="top:456px">
      <span>so.,&nbsp; 10.07.2011</span><span>10-18 uhr</span>
      <span>mo., 11.07.2011</span><span>10-14 uhr</span>
      <span>so.,&nbsp; 17.07.2011</span><span>10-18 uhr</span>
      <span>mo., 18.07.2011</span><span>10-14 uhr</span>
      <span>so.,&nbsp; 24.07.2011</span><span>10-18 uhr</span>
      <span>mo., 25.07.2011</span><span>10-14 uhr</span>
      <span>so.,&nbsp; 31.07.2011</span><span>10-18 uhr</span>
      <span>mo., 01.08.2011</span><span>10-14 uhr</span>
    </div>
    <h3 class="section-title" style="top:602px">voraussetzungen</h3>
    <p class="copy" style="top:626px">dieser kurs ist geeignet für friseure mit basiswissen, talentierte quereinsteiger und teilnehmer des ersten kurses, makeup basics.teilnehmer von makeup basics erhalten nach diesem kurs auch das junior makeup artist diplom.</p>
    <h3 class="section-title" style="top:710px">kosten</h3>
    <p class="copy" style="top:735px">€ 990 exkl. mwst.</p>
    <h3 class="section-title" style="top:756px">anmeldung</h3>
    <p class="copy" style="top:782px">bis 02.05.2011 mira@lockenglanzsalon.example oder 01 482 17 60</p>
  </section>

  <section class="column column--senior">
    <h2 class="course-title" style="top:56px">senior makeup artist</h2>
    <p class="copy" style="top:100px">in dir steckt ein künstler? du spielst gerne mit farben und formen? möchtest schminken für große bühnenshows und extravagante fotoshootings? dann solltest du unbedingt auch den dritten teil dieser visagistenausbildung absolvieren. hier lernst du makeups verschiedener epochen zu schminken aber auch abzuwandeln. in diesem workshop nehmen wir uns besonders viel zeit techniken zu perfektionieren und deiner makeupkunst eine individuelle note zu geben.</p>
    <h3 class="section-title" style="top:226px">inhalte auf einen blick</h3>
    <ul class="topics" style="top:253px">
      <li>- epochen makeup (20er bis 90er jahre)</li><li>- verschiedene kulturen / historische makeups</li>
      <li>(geisha, orientalisches makeup…)</li><li>- geschichte des makeup</li><li>- laufsteg makeup</li>
      <li>(konzepterstellung, makeup-design, planung)</li><li>- x-treme makeup / phantasie-makeup</li>
    </ul>
    <h3 class="section-title" style="top:428px">termine</h3>
    <div class="dates" style="top:449px">
      <span>so.,&nbsp; 11.09.2011</span><span>10-18 uhr</span>
      <span>mo., 12.09.2011</span><span>10-14 uhr</span>
      <span>so.,&nbsp; 18.09.2011</span><span>10-18 uhr</span>
      <span>mo., 19.09.2011</span><span>10-14 uhr</span>
      <span>so.,&nbsp; 25.09.2011</span><span>10-18 uhr</span>
      <span>mo., 26.09.2011</span><span>10-14 uhr</span>
      <span>so.,&nbsp; 02.10.2011</span><span>10-18 uhr</span>
      <span>mo., 03.10.2011</span><span>10-14 uhr</span>
    </div>
    <h3 class="section-title" style="top:600px">voraussetzungen</h3>
    <p class="copy" style="top:622px">dieser kurs ist geeignet für kreative künstler mit vorbildungund rundet die ausbildung für teilnehmer von teil 1 und 2(makeup basics und junior makeup artist) perfekt ab.der kurs endet mit einer schriftlichen und praktischen prüfung.teilnehmer, die auch die ersten beiden kurse besucht haben,erhalten nach bestandener prüfung ein visagistendiplom.</p>
    <h3 class="section-title" style="top:710px">kosten</h3>
    <p class="copy" style="top:735px">€ 990 exkl. mwst</p>
    <h3 class="section-title" style="top:756px">anmeldung</h3>
    <p class="copy" style="top:782px">bis 01.07.2011 mira@lockenglanzsalon.example oder 01 482 17 60bei anmeldung für alle drei kurse bis 01.03.2011,werden 5% rabatt auf den gesamtpreis gewährt</p>
  </section>
</main>
</body>
</html>
```